Bamboo Toothbrush packaging design

We need a packaging design for a pack of 4 bamboo toothbrushes. The front of the package would need to include the company logo, name of the product - Bamboo Toothbrush, 100% plastic free, and 10% of profit will go to environmental charities . Would like to see some simple or creative graphics to send the message.

Target Market(s)

Retail

Font styles to use
Sans Serif

Colors

Designer to choose colors to be used in the design.

Requirements
Must have
• Just be creative.

```html
<!DOCTYPE html>
<html lang="en">
<head>
<meta charset="utf-8">
<title>Bamboo Toothbrush Carton – Dieline</title>
<link href="https://fonts.googleapis.com/css2?family=Rubik:wght@400;500;700&display=swap" rel="stylesheet">
<style>
  :root{
    --ink:#1b313b;
    --leaf:#3bb54a;
    --kraft:#c4936a;
    --kraft-deep:#9c7a5c;
    --white:#ffffff;
    --cut:#e0303a;
    --fold:#5d6f77;
    --page:#ececec;
  }
  html,body{margin:0;padding:0;width:1200px;height:1024px;overflow:hidden;background:var(--page);}
  .canvas{width:1200px;height:1024px;display:flex;align-items:center;justify-content:center;
    background:radial-gradient(ellipse at center,#f7f7f7 0%,var(--page) 70%);}
  .dieline{width:1051px;height:402px;filter:drop-shadow(8px 10px 8px rgba(0,0,0,.25));}
  .dieline text{font-family:"Rubik",sans-serif;}
  .brand{font-weight:500;}
  .title{font-weight:700;}
  .bold{font-weight:700;}
</style>
</head>
<body>
<div class="canvas">
<svg class="dieline" viewBox="93 130 1314 502" xmlns="http://www.w3.org/2000/svg">
  <defs>
    <clipPath id="carton-shape">
      <path id="outline" d="M203,130 L1245,130 L1297,138 L1297,217 L1245,217 L1245,348 L1297,348 L1297,434 L1385,434 Q1407,434 1407,456 L1407,543 Q1407,565 1385,565 L1245,565 L1218,632 L278,632 L255,565 L255,434 L203,434 L203,348 L115,348 Q93,348 93,326 L93,239 Q93,217 115,217 L203,217 Z"/>
    </clipPath>

    <g id="front-face">
      <text class="brand" x="282" y="284" font-size="30" fill="var(--white)">Tallwind</text>
      <text class="title" x="283" y="334" font-size="34" fill="var(--leaf)">BAMBOO Toothbrush</text>
      <rect role="img" aria-label="Illustration of a bamboo toothbrush with white bristles" x="540" y="242" width="225" height="55" rx="6" fill="var(--kraft)"/>
      <rect role="img" aria-label="Silhouette illustration of bamboo stalks and leaves" x="790" y="222" width="300" height="122" fill="var(--kraft-deep)"/>
      <g class="badge">
        <rect x="1103" y="228" width="120" height="48" rx="24" fill="var(--leaf)"/>
        <circle cx="1127" cy="252" r="21" fill="var(--white)"/>
        <text x="1127" y="257" text-anchor="middle" class="bold" font-size="13" fill="var(--leaf)">100%</text>
        <text x="1159" y="243" class="bold" font-size="11" fill="var(--white)">100%</text>
        <text x="1159" y="257" class="bold" font-size="11" fill="var(--white)">PLASTIC</text>
        <text x="1159" y="271" class="bold" font-size="11" fill="var(--white)">FREE</text>
      </g>
      <g class="badge">
        <rect x="1103" y="290" width="120" height="48" rx="24" fill="var(--leaf)"/>
        <circle cx="1127" cy="314" r="21" fill="var(--white)"/>
        <g class="icon-leaf-hand" fill="var(--leaf)">
          <path d="M1120,312 C1120,302 1130,298 1138,300 C1138,309 1131,315 1120,312 Z"/>
          <path d="M1112,318 L1124,318 Q1130,318 1132,322 L1140,318 Q1143,318 1142,322 L1132,329 L1112,329 Z"/>
        </g>
        <text x="1155" y="302" class="bold" font-size="8.5" fill="var(--white)">10% of profit</text>
        <text x="1155" y="312" class="bold" font-size="8" fill="var(--white)">will go to</text>
        <text x="1155" y="322" class="bold" font-size="8" fill="var(--white)">environmental</text>
        <text x="1155" y="332" class="bold" font-size="8" fill="var(--white)">charities.</text>
      </g>
    </g>
  </defs>

  <!-- colour fields -->
  <g class="carton-fills" clip-path="url(#carton-shape)">
    <rect x="93" y="130" width="672" height="502" fill="var(--ink)"/>
    <rect x="765" y="130" width="20" height="502" fill="var(--leaf)"/>
    <rect x="785" y="130" width="622" height="502" fill="var(--kraft)"/>
  </g>

  <!-- fold lines -->
  <g class="folds" stroke="var(--fold)" stroke-width=".8" fill="none">
    <line x1="203" y1="217" x2="1245" y2="217"/>
    <line x1="203" y1="348" x2="1245" y2="348"/>
    <line x1="255" y1="434" x2="1245" y2="434"/>
    <line x1="255" y1="565" x2="1245" y2="565"/>
    <line x1="255" y1="130" x2="255" y2="565"/>
    <line x1="170" y1="217" x2="170" y2="348"/>
    <line x1="1245" y1="130" x2="1245" y2="565"/>
    <line x1="1330" y1="434" x2="1330" y2="565"/>
  </g>
  <use href="#outline" fill="none" stroke="var(--cut)" stroke-width="1"/>

  <!-- top tuck flap (upside down) -->
  <g class="top-flap" transform="rotate(180 517 172)">
    <text x="517" y="170" text-anchor="middle" class="bold" font-size="15" fill="var(--white)">Bamboo Toothbrush</text>
    <text x="517" y="190" text-anchor="middle" class="bold" font-size="15" fill="var(--white)">100% Plastic Free</text>
  </g>
  <text class="brand" transform="rotate(180 1152 158)" x="1152" y="167" text-anchor="middle" font-size="26" fill="var(--ink)">Tallwind</text>

  <!-- end flaps -->
  <text class="brand" transform="rotate(90 203 282)" x="203" y="288" text-anchor="middle" font-size="16" fill="var(--white)">Tallwind</text>
  <text class="brand" transform="rotate(-90 1297 500)" x="1297" y="506" text-anchor="middle" font-size="16" fill="var(--ink)">Tallwind</text>

  <!-- front panels -->
  <use class="front-panel" href="#front-face"/>
  <use class="front-panel" href="#front-face" transform="translate(0 217)"/>

  <!-- side panel -->
  <g class="side-panel">
    <text x="517" y="386" text-anchor="middle" class="bold" font-size="16" fill="var(--white)">Bamboo Toothbrush</text>
    <text x="517" y="407" text-anchor="middle" class="bold" font-size="16" fill="var(--white)">100% Plastic Free</text>
    <text x="801" y="374" font-size="8" fill="var(--ink)">distributed by:</text>
    <text x="801" y="389" font-size="12" fill="var(--ink)">Tallwind</text>
    <text x="801" y="412" font-size="9" fill="var(--ink)">MADE IN CHINA</text>
    <text class="brand" x="905" y="406" font-size="18" fill="var(--ink)">Tallwind</text>

    <g class="icon-recycle" fill="none" stroke="var(--ink)" stroke-width="2.4" stroke-linejoin="round">
      <path d="M1052,380 L1057,371 L1062,380"/>
      <path d="M1064,376 L1068,383 L1058,383"/>
      <path d="M1056,383 L1046,383 L1050,376"/>
      <path d="M1060,378 L1062,380 L1064,376" stroke-width="1.6"/>
    </g>
    <g class="icon-no-bin" fill="none" stroke="var(--ink)" stroke-width="1.4">
      <path d="M1083,368 L1097,368 M1085,368 L1087,383 L1093,383 L1095,368 M1088,365 L1092,365"/>
      <line x1="1080" y1="364" x2="1100" y2="386"/>
      <line x1="1100" y1="364" x2="1080" y2="386"/>
    </g>
  </g>
</svg>
</div>
</body>
</html>
```